Web Design For Metal Recycling Company

We are a scrap and recycling company dealing mainly in scrap metal base in Singapore. We deal in both domestic market and international market. Currently we are still unsure if we want to have a "lively" or "professional" company image so we will leave it to the designer to deem what is good.

We wish for a website to be able to "Retain" the interest of new visitor and at the same time able to give enough information for new and existing customer. We would also wish for design that will get the visitor to "Engage" us.

The attached is the logo for the company and we would want to incorporate that into the website. Either of the logo is fine.

```html
<!DOCTYPE html>
<html lang="en">
<head>
<meta charset="utf-8">
<title>Tan Kee Recycling</title>
<link href="https://fonts.googleapis.com/css2?family=Open+Sans:wght@600&family=Source+Sans+3:wght@400;600;700&display=swap" rel="stylesheet">
<style>
  :root{
    --gold:#cf9300;
    --gold-dark:#b27f00;
    --text:#4a4a4a;
    --nav:#5a5a5a;
    --dark:#222;
    --footer:#3b3b3b;
    --line:#c9c9c9;
    --card:#f7f5f0;
    --steel-light:#d4d6d8;
    --steel:#8f9296;
    --steel-dark:#2f3236;
  }
  *{box-sizing:border-box;margin:0;padding:0}
  html,body{width:1148px;height:1200px;overflow:hidden;background:#fff}
  body{position:relative;font-family:"Source Sans 3",Arial,sans-serif;color:var(--text)}
  .abs{position:absolute}
  .top-rule{left:0;top:0;width:1148px;height:4px;background:#7d7d7d}
  .header{left:0;top:4px;width:1148px;height:130px;background:linear-gradient(#fff,#f1f0f0)}
  .brand{left:135px;top:22px;width:175px;text-align:center}
  .brand-mark{width:50px;height:50px;border:3px solid var(--gold);margin:0 auto 12px}
  .brand-name{font-weight:700;font-size:16px;color:var(--gold);letter-spacing:1px;white-space:nowrap}
  .contact{right:135px;top:20px;text-align:right;color:var(--gold-dark)}
  .contact .phone{font-size:13px}
  .contact .phone b{font-weight:700}
  .contact .email{font-size:14px;margin-top:7px}
  .nav{top:78px;height:29px;font-size:11.7px;font-weight:600;color:var(--nav);line-height:29px;text-transform:uppercase;white-space:nowrap}
  .nav.active{background:var(--gold);color:#fff;width:59px;text-align:center;left:542px}
  .hero{left:0;top:134px;width:1148px;height:458px;
    background:
      radial-gradient(ellipse 220px 300px at 20% 40%,rgba(225,227,229,.75),rgba(225,227,229,0) 70%),
      radial-gradient(ellipse 200px 280px at 44% 55%,rgba(210,212,214,.7),rgba(210,212,214,0) 70%),
      radial-gradient(ellipse 360px 220px at 78% 55%,rgba(196,198,200,.65),rgba(196,198,200,0) 70%),
      radial-gradient(ellipse 260px 160px at 68% 20%,rgba(60,66,72,.55),rgba(60,66,72,0) 70%),
      radial-gradient(ellipse 200px 200px at 8% 85%,rgba(40,44,48,.6),rgba(40,44,48,0) 70%),
      radial-gradient(ellipse 160px 140px at 88% 88%,rgba(150,120,70,.35),rgba(150,120,70,0) 70%),
      linear-gradient(160deg,var(--steel) 0%,#6c7075 45%,var(--steel) 70%,#5b5f63 100%)}
  .dot{top:553px;width:12px;height:12px;border-radius:50%;background:#333}
  .dot.on{background:var(--gold);border:2px solid #fff}
  h2{position:absolute;font-family:"Open Sans",Arial,sans-serif;font-weight:600;font-size:21.5px;color:var(--gold);white-space:nowrap}
  .intro{left:135px;top:663px;width:620px;font-size:12.2px;line-height:24.2px}
  .more{font-size:14.5px;font-weight:600;color:var(--dark)}
  .services{left:790px;top:664px;list-style:none;font-size:12.2px}
  .services li{height:28.7px;line-height:24px;position:relative;padding-left:18px;white-space:nowrap}
  .services li::before{content:"";position:absolute;left:1px;top:10px;width:5px;height:5px;border-radius:50%;background:#333}
  .ribbon{left:933px;top:901px;width:80px;height:27px}
  .rule{left:135px;width:880px;border-top:1px dashed var(--line)}
  .card{top:943px;width:199px;height:128px;background:var(--card);box-shadow:0 0 3px rgba(0,0,0,.25)}
  .card .photo{position:absolute;left:9px;top:9px;width:180px;height:110px}
  .footer{left:0;top:1116px;width:1148px;height:84px;background:var(--footer);color:#fff}
  .foot-nav{left:135px;top:20px;font-size:11.5px;letter-spacing:.2px;white-space:nowrap}
  .copy{left:135px;top:48px;font-size:11.5px;color:#e6e6e6;white-space:nowrap}
  .social{top:22px;width:29px;height:29px;border-radius:50%}
</style>
</head>
<body>
  <div class="abs top-rule"></div>
  <header class="abs header"></header>
  <div class="abs brand">
    <div class="brand-mark"></div>
    <div class="brand-name">TAN KEE RECYCLING</div>
  </div>
  <div class="abs contact">
    <div class="phone"><b>PHONE :</b> +65 6100 2481</div>
    <div class="email">admin@tankeerecycling.example</div>
  </div>
  <div class="abs nav active">Home</div>
  <div class="abs nav" style="left:621px">About Us</div>
  <div class="abs nav" style="left:711px">Our Products</div>
  <div class="abs nav" style="left:833px">Our Services</div>
  <div class="abs nav" style="left:943px">Contact Us</div>

  <div class="abs hero" role="img" aria-label="Close-up of silver metal scrap shavings and spiral turnings"></div>
  <div class="abs dot on" style="left:551px"></div>
  <div class="abs dot" style="left:570px"></div>
  <div class="abs dot" style="left:589px"></div>

  <h2 style="left:134px;top:624px">Welcome to Our Company Site</h2>
  <p class="abs intro">Lorem ipsum dolor sit amet, consectetur adipisicing elit, sed do eiusmod tempor incididunt ut labore et dolore magna aliqua. Ut enim ad minim veniam, quis nostrud exercitation ullamco laboris nisi ut aliquip ex ea commodo consequat. Duis aute irure dolor in reprehenderit in voluptate velit esse cillum dolore eu fugiat nulla pariatur. Excepteur sint occaecat cupidatat non proident, magna aliqua. Ut enim ad minim veniam, quis nostrud exercitation ullamco laboris nisi ut aliquip ex ea commodo consequat. Duis aute irure dolor in reprehenderit sunt in culpa qui officia deserunt mollit anim id est laborume.Lorem ipsum dolor sit amet, consectetur adipisicing elit, sed do eiusmod tempor incidid-unt ut mollit anim id est laborum</p>
  <div class="abs more" style="left:135px;top:849px">Read More..</div>

  <h2 style="left:790px;top:624px">Our Services</h2>
  <ul class="abs services">
    <li>All grades of scrap</li>
    <li>All grades of aluminium/ stainless steel</li>
    <li>Electrical Cables/Wires</li>
    <li>Electronic Components</li>
    <li>Precious metal</li>
    <li>All other recyclable products</li>
  </ul>
  <div class="abs more" style="left:790px;top:850px">Read More..</div>

  <h2 style="left:134px;top:888px">Our Products</h2>
  <svg class="abs ribbon" viewBox="0 0 80 27" aria-label="View all products">
    <polygon points="3,3 73,3 80,13.5 73,24 3,24" fill="#9a6e00"/>
    <polygon points="0,0 72,0 78,13.5 72,27 0,27" fill="var(--gold)" transform="translate(1,0) scale(.98,.9)"/>
    <text x="39" y="16.5" text-anchor="middle" font-family="Source Sans 3, Arial, sans-serif" font-weight="700" font-size="10" fill="#fff">VIEW ALL</text>
  </svg>
  <div class="abs rule" style="top:934px"></div>

  <div class="abs card" style="left:136px"><div class="photo" role="img" aria-label="Steel pipe fittings and flanges" style="background:linear-gradient(135deg,#8a8d90,#4d5256 60%,#a3a6a8)"></div></div>
  <div class="abs card" style="left:363px"><div class="photo" role="img" aria-label="Bundle of stripped copper wire" style="background:linear-gradient(135deg,#e8a07d,#c4603a 50%,#f0b295)"></div></div>
  <div class="abs card" style="left:589px"><div class="photo" role="img" aria-label="Scrap valves and brass fittings" style="background:linear-gradient(135deg,#9a9e9a,#5f7d6c 45%,#b6b4ad)"></div></div>
  <div class="abs card" style="left:815px"><div class="photo" role="img" aria-label="Tangle of brass wire" style="background:linear-gradient(135deg,#d3c07a,#8f7a3a 50%,#cdbb86)"></div></div>
  <div class="abs rule" style="top:1080px"></div>

  <footer class="abs footer">
    <div class="abs foot-nav">HOME &nbsp;/&nbsp; ABOUT US &nbsp;/&nbsp; OUR PRODUCTS &nbsp;/&nbsp; OUR SERVICES &nbsp;/&nbsp; CONTACT US</div>
    <div class="abs copy">© 2014 Tan Kee All right reserved</div>
    <div class="abs social" style="left:911px;background:#3b5b98" aria-label="Social link"></div>
    <div class="abs social" style="left:947px;background:#2ba3dc" aria-label="Social link"></div>
    <div class="abs social" style="left:983px;background:#e33b2d" aria-label="Social link"></div>
  </footer>
</body>
</html>
```